Mobile Platform based Diabetes Management Service need flyer design

We need a flyer design for LuMaKai Service. We developed a mobile technology based platform where Diabetes patients can share their daily disease management information with their doctors and receive personalized advice. For more information, please check out www.lumakai-health.com.

We have a preliminary design for business card. and like to the flyer to go for similar style.

At this point, we are looking for framework draft only. Final wording on flyer will be in Chinese and we can insert that in later.

Target Market(s)

20 to 50 years old, smart phone users, diaganosed with Diabetes, health concisous,
full time working, busy, reluctant to schedule face to face doctor visit.

Industry/Entity Type

Business

Requirements
Must have
• The flyer should include LuMa Kai Logo. You can find the logo on the file I uploaded - the business card design file.

That being said, we also think LuMaKai logo can be a bit more flat. So please feel free to modify the logo design.
Nice to have
• We designed a "digital doctor" image - Dou Fen. You can include this cartoon figure as needed.

```html
<!DOCTYPE html>
<html lang="en">
<head>
<meta charset="utf-8">
<title>LuMaKai – Diabetes Management Flyer</title>
<link rel="stylesheet" href="https://fonts.googleapis.com/css2?family=Arimo:wght@400&family=Noto+Sans+SC:wght@400;700&display=swap">
<style>
  :root {
    --bg: #050505;
    --bg-glow: #2a2624;
    --text: #ffffff;
    --phone-body: #0b0b0b;
    --phone-rim: #6d6d6d;
    --screen-bg: #ffffff;
    --row-line: #e6e6e6;
    --status-bar: #000000;
    --header-green: #9ed63a;
    --header-green-dark: #7fb822;
    --tab-green: #0a7d12;
    --time-grey: #555555;
    --label-dark: #333333;
    --icon-red: #c8461a;
    --icon-green: #1fc41f;
    --icon-yellow: #f5cc15;
    --icon-blue: #86d3f2;
    --timeline: #d9d9d9;
  }
  * { margin: 0; padding: 0; box-sizing: border-box; }
  html, body { width: 848px; height: 1200px; overflow: hidden; background: var(--bg); }
  .flyer {
    position: relative; width: 848px; height: 1200px; overflow: hidden;
    background: var(--bg);
    font-family: "Arimo", "Helvetica Neue", Arial, sans-serif;
    color: var(--text);
  }
  .backdrop-figure {
    position: absolute; left: 0; top: 0; width: 520px; height: 1200px;
    background: radial-gradient(ellipse 300px 420px at 300px 430px, var(--bg-glow) 0%, rgba(20,18,17,0.6) 55%, transparent 100%);
  }
  .mascot {
    position: absolute; left: 36px; top: 157px; width: 114px; height: 192px;
    border-radius: 50px 50px 20px 20px;
    background: linear-gradient(180deg, #8a5a3a 0%, #e9d6c4 40%, #f2f2f2 70%, #c0392b 100%);
  }
  .headline {
    position: absolute; left: 162px; top: 160px;
    font-size: 62px; line-height: 64px; font-weight: 400; letter-spacing: -0.5px;
  }
  .body-copy {
    position: absolute; left: 40px; top: 397px; width: 350px;
    font-size: 17.6px; line-height: 24px;
  }
  .body-copy p + p { margin-top: 24px; }
  .brand { position: absolute; left: 40px; top: 975px; }
  .brand-name { font-size: 48px; line-height: 56px; font-weight: 400; }
  .brand-contact { margin-left: 6px; font-size: 18px; line-height: 23px; }

  .phone {
    position: absolute; left: 470px; top: -40px; width: 460px; height: 1224px;
    border-radius: 90px; background: var(--phone-body);
    border: 4px solid var(--phone-rim);
    box-shadow: inset 0 0 0 6px #1c1c1c, inset 0 0 0 8px #3a3a3a;
  }
  .phone-side-key {
    position: absolute; left: 464px; top: 368px; width: 6px; height: 100px;
    border-radius: 3px 0 0 3px; background: #5a5a5a;
  }
  .phone-speaker {
    position: absolute; left: 705px; top: 40px; width: 180px; height: 14px;
    border-radius: 7px; background: #2a2a2a; border: 1px solid #555;
  }
  .screen {
    position: absolute; left: 514px; top: 138px; width: 334px; height: 919px;
    background: var(--screen-bg); overflow: hidden;
    font-family: "Noto Sans SC", sans-serif;
  }
  .status-bar { height: 40px; background: var(--status-bar); display: flex; align-items: center; justify-content: flex-end; gap: 14px; }
  .status-icon { width: 18px; height: 18px; border-radius: 50%; border: 2px solid #bbb; }
  .app-header {
    height: 78px; background: linear-gradient(180deg, var(--header-green) 0%, var(--header-green-dark) 100%);
    display: flex; align-items: center; padding-left: 12px; gap: 52px;
  }
  .chart-button {
    width: 92px; height: 54px; border-radius: 8px; flex: none;
    background: linear-gradient(180deg, #5fb83a, #2e7d1a); border: 2px solid #1f4f10;
    color: #fff; font-size: 26px; font-weight: 700; display: flex; align-items: center; justify-content: center;
  }
  .header-date { color: #fff; font-size: 38px; font-weight: 700; white-space: nowrap; text-shadow: 0 1px 2px rgba(0,0,0,0.3); }
  .schedule { position: relative; }
  .schedule::before {
    content: ""; position: absolute; left: 138px; top: 0; bottom: 0; width: 2px; background: var(--timeline);
  }
  .entry { position: relative; border-bottom: 4px solid var(--row-line); }
  .entry-time { position: absolute; left: 17px; top: 14px; color: var(--time-grey); font-size: 21px; line-height: 30px; font-family: "Arimo", "Noto Sans SC", sans-serif; }
  .entry-icon {
    position: absolute; left: 117px; top: 18px; width: 44px; height: 44px; border-radius: 50%;
    display: flex; align-items: center; justify-content: center;
  }
  .entry-label { position: absolute; left: 193px; top: 14px; color: var(--label-dark); font-size: 27px; line-height: 34px; }
  .entry-detail { position: absolute; left: 193px; top: 92px; color: var(--label-dark); font-size: 21px; line-height: 31px; white-space: nowrap; }
  .icon-med { background: var(--icon-red); }
  .icon-drop { background: var(--icon-green); }
  .icon-meal { background: var(--icon-yellow); }
  .icon-sport { background: var(--icon-blue); }
  .tab-bar { position: absolute; left: 0; top: 831px; width: 400px; height: 88px; background: #fff; display: flex; }
  .tab { flex: none; width: 130px; text-align: center; padding-top: 22px; font-size: 30px; color: #777; white-space: nowrap; }
  .tab.is-last { width: 140px; }
  .tab.is-active { color: var(--tab-green); border-top: 10px solid var(--tab-green); border-bottom: 8px solid var(--tab-green); padding-top: 12px; }
</style>
</head>
<body>
<div class="flyer">
  <div class="backdrop-figure" role="img" aria-label="Faint, enlarged cartoon doctor figure fading into the dark background"></div>

  <div class="mascot" role="img" aria-label="Cartoon doctor character in a white coat with open arms"></div>
  <h1 class="headline">LOREM<br>IPSUM<br>DOLOR</h1>

  <div class="body-copy">
    <p>Lorem ipsum dolor sit amet, con-<br>sectetuer adipiscing elit, sed diam<br>nonummy nibh euismod tincidunt ut<br>laoreet dolore magna aliquam erat<br>volutpat. Ut wisi enim ad minim<br>veniam, quis nostrud exerci tation ulla-<br>mcorper suscipit lobortis nisl ut aliquip<br>ex ea commodo consequat.</p>
    <p>Duis autem vel eum iriure dolor in hen-<br>drerit in vulputate velit esse molestie<br>consequat, vel illum dolore eu feugiat<br>nulla facilisis at vero eros et accumsan<br>et iusto odio dignissim qui blandit<br>praesent luptatum zzril delenit augue<br>duis dolore te feugait nulla facilisi.</p>
    <p>Lorem ipsum dolor sit amet, con-<br>sectetuer adipiscing elit, sed diam<br>nonummy nibh euismod tincidunt ut<br>laoreet dolore magna aliquam erat<br>volutpat.</p>
  </div>

  <div class="brand">
    <div class="brand-name">LuMaKai</div>
    <div class="brand-contact">www.lumakai-health.com<br>+01 234 567 890</div>
  </div>

  <div class="phone"></div>
  <div class="phone-side-key"></div>
  <div class="phone-speaker"></div>

  <div class="screen">
    <div class="status-bar">
      <span class="status-icon"></span><span class="status-icon"></span><span class="status-icon"></span>
    </div>
    <div class="app-header">
      <div class="chart-button">图表</div>
      <div class="header-date">2013年5月</div>
    </div>
    <div class="schedule">
      <div class="entry" style="height:176px">
        <div class="entry-time">上午<br>08:03</div>
        <div class="entry-icon icon-med"><svg width="22" height="22" viewBox="0 0 22 22"><rect x="2" y="6" width="18" height="13" rx="2" fill="#fff"/><rect x="9" y="8" width="4" height="9" fill="#c8461a"/><rect x="6.5" y="10.5" width="9" height="4" fill="#c8461a"/></svg></div>
        <div class="entry-label">用药</div>
        <div class="entry-detail">氯磺丙脲[10<br>格列齐特(达</div>
      </div>
      <div class="entry" style="height:137px">
        <div class="entry-time">下午<br>12:03</div>
        <div class="entry-icon icon-drop"><svg width="20" height="22" viewBox="0 0 20 22"><path d="M10 2 C14 8 17 11 17 14 A7 7 0 0 1 3 14 C3 11 6 8 10 2Z" fill="#fff"/></svg></div>
        <div class="entry-label">测血压</div>
      </div>
      <div class="entry" style="height:133px">
        <div class="entry-time">下午<br>13:06</div>
        <div class="entry-icon icon-meal"><svg width="22" height="18" viewBox="0 0 22 18"><path d="M2 7 H20 A9 9 0 0 1 2 7Z" fill="#fff"/></svg></div>
        <div class="entry-label">晚餐</div>
      </div>
      <div class="entry" style="height:132px">
        <div class="entry-time">下午<br>15:06</div>
        <div class="entry-icon icon-sport"><svg width="24" height="12" viewBox="0 0 24 12"><rect x="6" y="5" width="12" height="2" fill="#fff"/><path d="M1 6 L7 1 V11Z M23 6 L17 1 V11Z" fill="#fff"/></svg></div>
        <div class="entry-label">游泳</div>
      </div>
      <div class="entry" style="height:133px; border-bottom:none">
        <div class="entry-time">下午<br>16:01</div>
        <div class="entry-icon icon-drop"><svg width="20" height="22" viewBox="0 0 20 22"><path d="M10 2 C14 8 17 11 17 14 A7 7 0 0 1 3 14 C3 11 6 8 10 2Z" fill="#fff"/></svg></div>
        <div class="entry-label">晚餐后血<br>糖</div>
      </div>
    </div>
    <div class="tab-bar">
      <div class="tab is-active">管理</div>
      <div class="tab">知识</div>
      <div class="tab is-last">消息</div>
    </div>
  </div>
</div>
</body>
</html>
```